Visitenkarte und Briefpapier für Rechtsanwaltskanzlei
Zielgruppe
Neugründung einer Rechtsanwaltskanzlei für Strafrecht mit einem Anwalt
Aufgabenstellung
Ich möchte gerne Briefpapier und Visitenkarten mit einem schlichten aber professionellen Charakter für meine neue Rechtsanwaltskanzlei erstellen lassen. Die Erscheinung soll modern, sachlich und klar sein. Es soll kein Logo verwendet werden, sondern nur der Namensschriftzug "Dr. Harald Obst", gerne in Großbuchstaben. Siehe dazu beispielhaft die Design-Charakter der angegeben Links.
Die Visitenkarte sollen als druckfähiges PDF und das Briefpapier zusätzlich als Word-Dokument geliefert werden.

```html
<!DOCTYPE html>
<html lang="de">
<head>
<meta charset="utf-8">
<title>Dr. Harald Obst – Geschäftsausstattung</title>
<link rel="stylesheet" href="https://fonts.googleapis.com/css2?family=Jost:wght@300;400;500&family=Josefin+Slab:wght@400&display=swap">
<style>
  :root {
    --ink: #1e1e1e;
    --muted: #9a9a9a;
    --paper: #ffffff;
    --stage: #d5d5d5;
    --frame: #3a3a3a;
    --body: #4a4a4a;
  }
  html, body { margin: 0; padding: 0; }
  body {
    width: 1200px; height: 2399px; overflow: hidden;
    position: relative; background: var(--paper);
    font-family: "Jost", "Century Gothic", sans-serif; color: var(--ink);
  }
  .brand-title {
    position: absolute; top: 196px; left: 0; width: 1200px; margin: 0;
    text-align: center; font-weight: 500; font-size: 56px; letter-spacing: 2px;
    line-height: 1; color: var(--ink);
  }
  .stage { position: absolute; left: 0; width: 1200px; background: var(--stage); }
  .stage--cards { top: 816px; height: 483px; }
  .stage--letter { top: 1352px; height: 893px; }

  .card {
    position: absolute; width: 487px; height: 305px; box-sizing: border-box;
    background: var(--paper);
  }
  .card--outlined { border: 1px solid var(--frame); }
  .card--plain { border: 1px solid #c4c4c4; }
  .card__name {
    position: absolute; left: 41px; top: 56px; margin: 0;
    font-weight: 500; font-size: 26px; letter-spacing: 0.6px; line-height: 1; white-space: nowrap;
  }
  .card__tagline {
    position: absolute; left: 41px; top: 93px; margin: 0;
    font-weight: 300; font-size: 11px; letter-spacing: 0.2px; color: var(--muted);
    text-transform: uppercase; white-space: nowrap;
  }
  .card__address, .card__contact {
    position: absolute; top: 183px; margin: 0; font-style: normal;
    font-weight: 300; font-size: 14px; line-height: 21.5px; white-space: nowrap;
  }
  .card__address { left: 40px; }
  .card__contact { left: 277px; display: grid; grid-template-columns: 62px auto; }

  .letterhead {
    position: absolute; left: 274px; top: 1448px; width: 486px; height: 685px;
    background: #fbfbfb;
  }
  .letterhead__name {
    position: absolute; left: 72px; top: 88px; margin: 0;
    font-weight: 500; font-size: 13px; letter-spacing: 0.3px; white-space: nowrap;
  }
  .letterhead__tagline {
    position: absolute; left: 72px; top: 106px; margin: 0;
    font-weight: 300; font-size: 5.6px; color: var(--muted); text-transform: uppercase; white-space: nowrap;
  }
  .letterhead__body {
    position: absolute; left: 68px; top: 211px; width: 350px;
    font-family: "Josefin Slab", Georgia, serif; font-size: 8.6px; line-height: 8.35px;
    color: var(--body); text-align: justify; hyphens: auto;
  }
  .letterhead__body p { margin: 0 0 8.4px; }

  .mini-card {
    position: absolute; left: 824px; top: 1502px; width: 198px; height: 128px;
    background: #fbfbfb;
  }
  .mini-card__name {
    position: absolute; left: 19px; top: 41px; margin: 0;
    font-weight: 500; font-size: 11.5px; letter-spacing: 0.3px; white-space: nowrap;
  }
  .mini-card__tagline {
    position: absolute; left: 19px; top: 58px; margin: 0;
    font-weight: 300; font-size: 5px; color: var(--muted); text-transform: uppercase; white-space: nowrap;
  }
</style>
</head>
<body>

<h1 class="brand-title">DR. HARALD OBST</h1>

<section class="card card--outlined" style="left:83px; top:457px;">
  <p class="card__name">DR. HARALD OBST</p>
  <p class="card__tagline">Rechtsanwaltskanzlei für Strafrecht</p>
</section>
<section class="card card--outlined" style="left:621px; top:457px;">
  <address class="card__address">Dr. Harald Obst<br>Kastanienweg 4<br>84034 Oberwangen</address>
  <div class="card__contact">
    <span>telefon:</span><span>08123 – 55 21 40</span>
    <span>telefax:</span><span>08123 – 55 21 41</span>
    <span>e-mail:</span><span>dr.obst@postfeld.de</span>
  </div>
</section>

<div class="stage stage--cards"></div>
<section class="card card--plain" style="left:83px; top:905px;">
  <p class="card__name">DR. HARALD OBST</p>
  <p class="card__tagline">Rechtsanwaltskanzlei für Strafrecht</p>
</section>
<section class="card card--plain" style="left:621px; top:905px;">
  <address class="card__address">Dr. Harald Obst<br>Kastanienweg 4<br>84034 Oberwangen</address>
  <div class="card__contact">
    <span>telefon:</span><span>08123 – 55 21 40</span>
    <span>telefax:</span><span>08123 – 55 21 41</span>
    <span>e-mail:</span><span>dr.obst@postfeld.de</span>
  </div>
</section>

<div class="stage stage--letter"></div>
<section class="letterhead">
  <p class="letterhead__name">DR. HARALD OBST</p>
  <p class="letterhead__tagline">Rechtsanwaltskanzlei für Strafrecht</p>
  <div class="letterhead__body" lang="la">
    <p>Lorem ipsum dolor sit amet,</p>
    <p>Lorem ipsum dolor sit amet, consectetur adipiscing elit. Donec orci purus, luctus vitae dignissim eu, iaculis sed purus. Vivamus faucibus, ipsum nec aliquet viverra, leo mauris condimentum ligula, sit amet sagittis enim ligula quis arcu. Nam egestas tortor id nisi porttitor mattis. In tortor ante, ultricies in suscipit a, tempus non massa. Vivamus et auctor mi. Fusce vel massa nulla. Phasellus nec eros mauris, et scelerisque orci. Donec malesuada orci vitae nulla accumsan porta a id massa. Quisque accumsan iaculis magna sit amet fringilla. Maecenas consequat, magna eget tincidunt semper, odio nibh rutrum mi, id feugiat ante nisi eu risus. Vestibulum nunc orci, rhoncus a placerat in, ultricies in mi. Cras mattis varius eros, vel fringilla nisi suscipit eget.</p>
    <p>Quisque scelerisque sagittis nulla at porttitor. Mauris a justo et tellus interdum tristique. Sed id augue vitae urna euismod commodo aliquet a quam. Pellentesque arcu velit, cursus et malesuada ut, consequat et diam. Nullam erat sem, rhoncus id ullamcorper vitae, rhoncus et arcu. In ultricies ultricies nulla, ut rutrum nisi iaculis at. Donec eu magna a metus ornare faucibus. Fusce aliquet faucibus ultricies. Morbi semper, est id tincidunt gravida, sem arcu adipiscing lacus, ac bibendum nulla leo eu purus. Quisque nec diam sed risus consectetur a cumsan quis quis nibh. Vestibulum id purus lorem.</p>
    <p>Vivamus vehicula accumsan lacinia. Aliquam erat volutpat. Pellentesque consequat venenatis velit non gravida. Etiam et sem et nulla congue aliquam sed eget augue. Nulla facilisi. Pellentesque habitant morbi tristique senectus et netus et malesuada fames ac turpis egestas. Nulla a elit at sem iaculis congue. Nullam mollis tristique lobortis.</p>
  </div>
</section>
<section class="mini-card">
  <p class="mini-card__name">DR. HARALD OBST</p>
  <p class="mini-card__tagline">Rechtsanwaltskanzlei für Strafrecht</p>
</section>

</body>
</html>
```